iWebSentry flyer internet security for families

We need a flyer design A5 size for distribution by hand and in magazines.

iWebSentry is a service used to protect families online when using all types of devices, on Wi-Fi and mobile network connections.

the website is www.iwebsentry-demo.co.uk

The ad should communicate ease of use, and should be aimed at parents with children between the ages of 3-18. The advert should be communicative but not have lots of text or words.

attached logo designs.

Reason: Extended deadline as have not had time to review the designs due to preparing for service launch on Monday

Industry/Entity Type

Internet

Requirements
Must have
• The 30 day free trial
• Icons for the different platforms that it works on
• emphasis on the features of the product without too much text
• web address www.iwebsentry-demo.co.uk
• info@iwebsentry-demo.co.uk
Nice to have
• A picture of a family including grandparents, parents and children all using devices.
Should not have
• Any of the pricing
• Too much text

```html
<!DOCTYPE html>
<html lang="en">
<head>
<meta charset="utf-8">
<title>iWebSentry – 30 Day Free Trial Flyer</title>
<link href="https://fonts.googleapis.com/css2?family=Source+Sans+3:wght@400;600;700&display=swap" rel="stylesheet">
<style>
  :root{
    --navy:#0b4f7c;
    --deep:#0a4168;
    --blue:#1582c2;
    --sky:#2a9fd9;
    --steel:#5c98b9;
    --mist:#dfe3e6;
    --grey:#c9ccce;
    --orange:#f07a1a;
    --ink:#3c3c3c;
    --paper:#ffffff;
    --backdrop:#ececec;
  }
  *{box-sizing:border-box;margin:0;padding:0}
  html,body{width:1200px;height:1200px;overflow:hidden;background:var(--backdrop)}
  body{font-family:"Source Sans 3",sans-serif;color:var(--ink)}
  .flyer{position:absolute;left:190px;top:20px;width:820px;height:1160px;background:var(--paper);overflow:hidden;box-shadow:0 4px 18px rgba(0,0,0,.12)}
  .flyer-shapes{position:absolute;inset:0}
  .brand{position:absolute;right:40px;top:50px;display:flex;align-items:center;gap:10px}
  .brand-dot{width:32px;height:32px;border-radius:50%;background:var(--blue)}
  .brand-name{font-size:34px;font-weight:700;color:var(--blue);letter-spacing:.5px;line-height:1}
  .offer{position:absolute;left:340px;top:462px;color:#fff;line-height:1}
  .offer-the{font-size:52px;font-weight:400}
  .offer-num{font-size:118px;font-weight:700;letter-spacing:-3px}
  .offer-day{font-size:50px;font-weight:700;margin-left:6px}
  .offer-trial{font-size:44px;font-weight:700;margin-top:-2px}
  .feature-column{position:absolute;top:752px;width:385px;display:flex;flex-direction:column;gap:12px}
  .feature-column--left{left:28px;gap:22px;top:762px}
  .feature-column--right{left:412px}
  .feature{display:flex;gap:14px;align-items:flex-start}
  .feature-icon{flex:0 0 56px;height:56px}
  .feature h2{font-size:17px;font-weight:700;color:var(--navy);margin-bottom:3px;line-height:1.15}
  .feature p{font-size:12.5px;line-height:1.35;text-align:justify}
  .footer{position:absolute;left:0;bottom:0;height:60px;width:620px;background:var(--blue);border-radius:0 60px 0 0;color:#fff;font-weight:700;font-size:18px;white-space:nowrap;display:flex;align-items:center;padding-left:30px}
</style>
</head>
<body>
<main class="flyer">
  <svg class="flyer-shapes" viewBox="0 0 820 1160" width="820" height="1160">
    <defs>
      <linearGradient id="photoTone" x1="0" y1="0" x2="1" y2="1">
        <stop offset="0" stop-color="#9cc6e2"/>
        <stop offset=".55" stop-color="#d9c2b0"/>
        <stop offset="1" stop-color="#5a6b80"/>
      </linearGradient>
      <clipPath id="upperArea"><rect x="0" y="0" width="820" height="735"/></clipPath>
    </defs>
    <circle cx="330" cy="1110" r="230" fill="#eef0f1"/>
    <g clip-path="url(#upperArea)">
      <g fill="var(--mist)">
        <rect x="600" y="-30" width="360" height="36" rx="18" transform="rotate(45 600 -30)"/>
        <rect x="720" y="420" width="300" height="32" rx="16" transform="rotate(45 720 420)"/>
      </g>
      <path d="M0 0 H440 L0 440 Z" fill="var(--blue)"/>
      <g fill="var(--navy)">
        <rect x="-120" y="160" width="720" height="150" rx="75" transform="rotate(45 -120 160)"/>
        <rect x="-200" y="380" width="640" height="130" rx="65" transform="rotate(45 -200 380)"/>
      </g>
      <rect x="-40" y="340" width="460" height="16" rx="8" fill="#6ea6c9" transform="rotate(45 -40 340)"/>
      <rect x="-60" y="500" width="360" height="14" rx="7" fill="#fff" opacity=".85" transform="rotate(45 -60 500)"/>
      <line x1="450" y1="-10" x2="700" y2="240" stroke="var(--deep)" stroke-width="40" stroke-linecap="round"/>
      <path d="M820 230 Q820 330 720 330 Q660 330 620 290" fill="none" stroke="var(--deep)" stroke-width="20" stroke-linecap="round"/>
      <circle cx="810" cy="560" r="75" fill="var(--steel)"/>
      <circle cx="470" cy="500" r="240" fill="var(--grey)"/>
      <circle cx="463" cy="497" r="235" fill="var(--navy)"/>
      <path d="M40 40 H450 Q560 40 560 150 V320 Q560 420 470 420 H300 Q240 420 220 470 Q180 500 120 470 Q40 440 40 360 Z" fill="var(--sky)"/>
      <path d="M52 52 H440 Q540 52 540 150 V312 Q540 404 460 404 H300 Q236 404 214 452 Q180 480 124 456 Q52 430 52 360 Z" fill="url(#photoTone)" role="img" aria-label="Photo of a family with grandparents, parents and a child using a laptop and tablets"/>
    </g>
  </svg>

  <div class="brand"><span class="brand-dot"></span><span class="brand-name">iWebSentry</span></div>

  <div class="offer">
    <div class="offer-the">The</div>
    <div><span class="offer-num">30</span><span class="offer-day">day</span></div>
    <div class="offer-trial">FREE TRIAL</div>
  </div>

  <div class="feature-column feature-column--left">
    <section class="feature">
      <svg class="feature-icon" viewBox="0 0 62 62"><circle cx="18" cy="32" r="14" fill="var(--orange)"/><circle cx="44" cy="32" r="14" fill="var(--blue)"/></svg>
      <div><h2>Supports Multiple Devices</h2><p>Supported on Winframe, Droidly, iOrbit and Kindra devices.</p></div>
    </section>
    <section class="feature">
      <svg class="feature-icon" viewBox="0 0 62 62"><rect x="3" y="8" width="56" height="38" rx="3" fill="none" stroke="var(--orange)" stroke-width="4"/><rect x="26" y="46" width="10" height="8" fill="var(--orange)"/><rect x="12" y="32" width="6" height="10" fill="var(--blue)"/><rect x="22" y="26" width="6" height="16" fill="var(--blue)"/><rect x="32" y="30" width="6" height="12" fill="var(--blue)"/><rect x="42" y="22" width="6" height="20" fill="var(--blue)"/><polyline points="10,26 22,18 34,22 50,12" fill="none" stroke="var(--orange)" stroke-width="3"/></svg>
      <div><h2>Dashboard to monitor usage</h2><p>Shows the top 10 sites visited, amount of time spent on those sites, top 10 sites blocked sites, amount of bandwidth consumed and can be filtered per user basis for the last day, week and month.</p></div>
    </section>
    <section class="feature">
      <svg class="feature-icon" viewBox="0 0 62 62"><rect x="8" y="8" width="46" height="30" rx="3" fill="none" stroke="var(--blue)" stroke-width="4"/><rect x="2" y="30" width="14" height="24" rx="2" fill="#fff" stroke="var(--blue)" stroke-width="3"/><rect x="46" y="32" width="12" height="22" rx="2" fill="#fff" stroke="var(--blue)" stroke-width="3"/><circle cx="31" cy="24" r="9" fill="none" stroke="var(--orange)" stroke-width="3"/><line x1="31" y1="24" x2="36" y2="19" stroke="var(--orange)" stroke-width="3"/></svg>
      <div><h2>Limit Device Bandwidth Utilisation</h2><p>The amount of bandwidth (i.e. the amount of data that the device downloads) can be limited. This is particularly useful for households who pay for a set amount of data usage a month.</p></div>
    </section>
  </div>

  <div class="feature-column feature-column--right">
    <section class="feature">
      <svg class="feature-icon" viewBox="0 0 62 62"><rect x="3" y="6" width="48" height="40" rx="3" fill="none" stroke="var(--orange)" stroke-width="4"/><line x1="3" y1="15" x2="51" y2="15" stroke="var(--orange)" stroke-width="3"/><ellipse cx="27" cy="30" rx="14" ry="8" fill="none" stroke="var(--orange)" stroke-width="3"/><circle cx="27" cy="30" r="4" fill="var(--orange)"/><circle cx="50" cy="48" r="9" fill="var(--blue)"/><circle cx="50" cy="48" r="3" fill="#fff"/></svg>
      <div><h2>See what websites have been visited</h2><p>You are able to see reports on which websites have been visited and how long has been spent on these websites.</p></div>
    </section>
    <section class="feature">
      <svg class="feature-icon" viewBox="0 0 62 62"><rect x="3" y="8" width="46" height="34" rx="3" fill="none" stroke="var(--blue)" stroke-width="4"/><line x1="3" y1="16" x2="49" y2="16" stroke="var(--blue)" stroke-width="3"/><text x="8" y="32" font-size="11" font-weight="700" fill="var(--blue)" font-family="Source Sans 3, sans-serif">www</text><rect x="36" y="36" width="22" height="20" rx="2" fill="var(--orange)"/><path d="M41 36 V30 a6 6 0 0 1 12 0 V36" fill="none" stroke="var(--orange)" stroke-width="3"/></svg>
      <div><h2>Block Inappropriate Content</h2><p>Restrictions can be placed onto the device so that users cannot visit sites deemed inappropriate including phishing sites which is a site that purports to be a well known site (commonly a financial institution) in order to trick you into entering in your login details in order to gain access to those services</p></div>
    </section>
    <section class="feature">
      <svg class="feature-icon" viewBox="0 0 62 62"><rect x="3" y="8" width="44" height="40" rx="3" fill="none" stroke="var(--orange)" stroke-width="4"/><rect x="3" y="8" width="44" height="9" fill="var(--orange)"/><g fill="var(--orange)"><rect x="9" y="22" width="7" height="6"/><rect x="20" y="22" width="7" height="6"/><rect x="31" y="22" width="7" height="6"/><rect x="9" y="32" width="7" height="6"/><rect x="20" y="32" width="7" height="6"/></g><circle cx="46" cy="44" r="12" fill="#fff" stroke="var(--blue)" stroke-width="4"/><polyline points="46,37 46,44 51,47" fill="none" stroke="var(--blue)" stroke-width="3"/></svg>
      <div><h2>Device Access Times</h2><p>The device can be set so that it can only connect to the Internet for certain periods of the day such as between 4PM and 7PM. Limitations can be set so that the device can only access the Internet for a certain period of time in 24 hours, such as 2 hours of usage every 24 hours.</p></div>
    </section>
  </div>

  <footer class="footer">www.iwebsentry-demo.co.uk&nbsp;|&nbsp;info@iwebsentry-demo.co.uk</footer>
</main>
</body>
</html>
```